Craft Beer Needs a Label/ Logo Design

Name: Lanternfall
(Lanternfall Ale, Lanternfall Pilsner, Lanternfall Stout)

We are looking for a logo-ed label that will resonate domestically and internationally for this new Craft Beer Brand.

Target Market(s)

Millenials

Logo Text

Lanternfall Pilsner

Logo styles of interest
Emblem Logo
Character Logo
Colors

Designer to choose colors to be used in the design.

Requirements
Must have
• A labled logo design -- "Lanternfall" is the name, but would like to see samples with "Ale", "Pilsner", or "Stout" after!

```html
<!DOCTYPE html>
<html lang="en">
<head>
<meta charset="utf-8">
<title>Lanternfall Craft Beer Labels</title>
<link rel="stylesheet" href="https://fonts.googleapis.com/css2?family=Exo+2:wght@400;600;800&family=Pinyon+Script&display=swap">
<style>
  :root {
    --page-top: #0d0d0d;
    --page-bottom: #e9e9e9;
    --amber: #c9741a;
    --amber-light: #e39a3a;
    --ink: #0a0a0a;
    --paper: #ffffff;
    --rule: #f3f3f3;
    --ridge: #151515;
  }
  * { box-sizing: border-box; margin: 0; padding: 0; }
  html, body { width: 1200px; height: 944px; overflow: hidden; }
  body {
    background: linear-gradient(180deg, var(--page-top) 0%, #555 45%, var(--page-bottom) 100%);
    font-family: "Exo 2", Arial, sans-serif;
    color: var(--paper);
  }
  .label-range {
    display: flex;
    justify-content: center;
    gap: 45px;
    padding-top: 175px;
  }
  .variant { width: 250px; display: flex; flex-direction: column; align-items: center; }

  .variant--stout   { --sky-deep: #080808; --sky-glow: #6c6c6c; --accent: #d2d2d2; }
  .variant--lager   { --sky-deep: #031006; --sky-glow: #21b02c; --accent: #34d640; }
  .variant--pilsner { --sky-deep: #170804; --sky-glow: #bd5520; --accent: #e4672a; }
  .variant--ale     { --sky-deep: #050a26; --sky-glow: #1f82dc; --accent: #3a9df2; }

  /* neck label */
  .neck-label {
    width: 170px; height: 120px;
    background: linear-gradient(90deg, var(--ink) 0%, var(--ink) 55%, var(--sky-glow) 130%);
    border-top: 5px solid var(--rule);
    border-bottom: 5px solid var(--rule);
    display: flex; flex-direction: column; align-items: center; justify-content: center;
    text-align: center;
  }
  .neck-label__name { font-weight: 800; font-size: 17px; letter-spacing: 0.5px; text-transform: uppercase; }
  .neck-label__style { font-size: 13px; margin-top: 3px; }
  .neck-label__tagline { font-family: "Pinyon Script", cursive; font-size: 15px; margin-top: 10px; color: #e8e8e8; }

  /* body label */
  .body-label {
    margin-top: 50px; width: 250px; height: 410px;
    display: flex; flex-direction: column;
    background: var(--ink);
  }
  .body-label__crown {
    height: 52px; background: linear-gradient(180deg, var(--amber-light), var(--amber));
    display: flex; align-items: center; justify-content: center;
    font-size: 13px; font-weight: 600; color: var(--ink);
  }
  .stripes {
    height: 9px;
    background: repeating-linear-gradient(180deg, var(--amber) 0 1px, #5a300a 1px 3px);
  }
  .body-label__sky {
    position: relative; height: 260px;
    background: radial-gradient(ellipse 120% 70% at 50% 100%, var(--sky-glow) 0%, var(--sky-deep) 75%);
    display: flex; flex-direction: column; align-items: center;
  }
  .body-label__name {
    margin-top: 62px; font-weight: 800; font-size: 30px; letter-spacing: 0.5px;
    text-transform: uppercase; color: var(--paper);
  }
  .body-label__style { font-size: 22px; margin-top: 6px; }
  .body-label__landscape {
    position: absolute; left: 0; right: 0; bottom: 0; height: 70px;
    background: linear-gradient(180deg, #2a2a2a 0%, var(--ridge) 100%);
  }
  .body-label__base {
    flex: 1; background: var(--ridge);
    display: flex; align-items: center; justify-content: center;
    font-size: 11px; letter-spacing: 1.5px; text-transform: uppercase; color: var(--accent);
  }
</style>
</head>
<body>
<main class="label-range">

  <section class="variant variant--stout">
    <div class="neck-label">
      <p class="neck-label__name">Lanternfall</p>
      <p class="neck-label__style">Stout</p>
      <p class="neck-label__tagline">Take the Lanternfall Road</p>
    </div>
    <div class="body-label">
      <p class="body-label__crown">Craft Beer Brewing Company</p>
      <div class="stripes"></div>
      <div class="body-label__sky">
        <h2 class="body-label__name">Lanternfall</h2>
        <p class="body-label__style">Stout</p>
        <div class="body-label__landscape" role="img" aria-label="Silhouette of desert mesas and rock spires at night"></div>
      </div>
      <p class="body-label__base">Arizona, US</p>
      <div class="stripes"></div>
    </div>
  </section>

  <section class="variant variant--lager">
    <div class="neck-label">
      <p class="neck-label__name">Lanternfall</p>
      <p class="neck-label__style">Lager</p>
      <p class="neck-label__tagline">Take the Lanternfall Road</p>
    </div>
    <div class="body-label">
      <p class="body-label__crown">Craft Beer Brewing Company</p>
      <div class="stripes"></div>
      <div class="body-label__sky">
        <h2 class="body-label__name">Lanternfall</h2>
        <p class="body-label__style">Lager</p>
        <div class="body-label__landscape" role="img" aria-label="Silhouette of desert mesas and rock spires at night"></div>
      </div>
      <p class="body-label__base">Arizona, US</p>
      <div class="stripes"></div>
    </div>
  </section>

  <section class="variant variant--pilsner">
    <div class="neck-label">
      <p class="neck-label__name">Lanternfall</p>
      <p class="neck-label__style">Pilsner</p>
      <p class="neck-label__tagline">Take the Lanternfall Road</p>
    </div>
    <div class="body-label">
      <p class="body-label__crown">Craft Beer Brewing Company</p>
      <div class="stripes"></div>
      <div class="body-label__sky">
        <h2 class="body-label__name">Lanternfall</h2>
        <p class="body-label__style">Pilsner</p>
        <div class="body-label__landscape" role="img" aria-label="Silhouette of desert mesas and rock spires at night"></div>
      </div>
      <p class="body-label__base">Arizona, US</p>
      <div class="stripes"></div>
    </div>
  </section>

  <section class="variant variant--ale">
    <div class="neck-label">
      <p class="neck-label__name">Lanternfall</p>
      <p class="neck-label__style">Ale</p>
      <p class="neck-label__tagline">Take the Lanternfall Road</p>
    </div>
    <div class="body-label">
      <p class="body-label__crown">Craft Beer Brewing Company</p>
      <div class="stripes"></div>
      <div class="body-label__sky">
        <h2 class="body-label__name">Lanternfall</h2>
        <p class="body-label__style">Ale</p>
        <div class="body-label__landscape" role="img" aria-label="Silhouette of desert mesas and rock spires at night"></div>
      </div>
      <p class="body-label__base">Arizona, US</p>
      <div class="stripes"></div>
    </div>
  </section>

</main>
</body>
</html>
```